Website for a Construction Business That Builds Houses

We want some design concepts for this website. Customer likes this competitor site: https://copperfernbuilds.com.au/

We have a logo for Varrow Constructions. Logo font is Birdman, attached with AI.

Want to be able to change hero images

Will have a contact page.

Need to know what plugins will be used for WordPress.

```html
<!DOCTYPE html>
<html lang="en">
<head>
<meta charset="utf-8">
<title>Varrow Constructions</title>
<link href="https://fonts.googleapis.com/css2?family=Libre+Baskerville:wght@400;700&family=Poppins:wght@400;500;600&display=swap" rel="stylesheet">
<style>
:root{
  --ink:#111;
  --black:#000;
  --white:#fff;
  --grey-panel:#e3e3e3;
  --field:#dcdcdc;
  --muted:#8a8a8a;
  --text:#444;
  --hero-sky:#a9a7cf;
  --overlay:rgba(40,38,30,.88);
  --serif:"Libre Baskerville",Georgia,serif;
  --sans:"Poppins",Arial,sans-serif;
}
*{box-sizing:border-box;margin:0;padding:0}
html,body{width:1200px;height:3014px;overflow:hidden;background:var(--white)}
body{position:relative;font-family:var(--sans);color:var(--ink)}
.abs{position:absolute}
.ph{position:absolute}
.label{font-family:var(--sans);font-weight:600;font-size:10.5px;letter-spacing:1.6px;text-transform:uppercase}
.h2{font-family:var(--serif);font-weight:400;font-size:20px;line-height:25px}
.body{font-size:10.5px;line-height:15.5px}
.link-arrow{font-size:10px;font-weight:600;letter-spacing:1px;text-transform:uppercase;border-bottom:1.5px solid currentColor;padding-bottom:2px;display:inline-flex;align-items:center;gap:6px}

/* hero */
.hero{left:0;top:0;width:1200px;height:585px;background:linear-gradient(180deg,#8f93c6 0%,#b7b2d6 35%,#d9b9b6 55%,#6f6a74 70%,#4d5260 100%)}
.topbar{left:185px;top:0;width:831px;height:25px;border-bottom:1px solid rgba(255,255,255,.5);display:flex;align-items:center;justify-content:space-between;color:var(--white);font-size:8.5px}
.topbar .info{display:flex;gap:16px;align-items:center}
.topbar .info span{display:flex;align-items:center;gap:6px}
.topbar .social{display:flex;gap:5px}
.topbar .social i{width:12px;height:12px;border:1px solid var(--white);border-radius:50%;display:block}
.nav{left:185px;top:46px;width:831px;display:flex;justify-content:space-between;align-items:center;color:var(--white)}
.brand{display:flex;align-items:center;gap:7px;font-family:var(--sans);font-weight:500;font-size:15px}
.brand i{width:10px;height:10px;border-radius:50%;background:currentColor;display:block}
.menu{display:flex;gap:16px;font-size:12px;font-weight:500}
.hero-box{left:184px;top:370px;width:583px;height:215px;background:var(--overlay);color:var(--white);padding:30px 34px}
.hero-box h1{font-family:var(--serif);font-weight:700;font-size:29px;line-height:36px}
.hero-box p{margin-top:12px;font-size:10.2px;line-height:15px;width:510px}
.pager{position:absolute;left:46px;top:187px;display:flex;align-items:center;gap:16px;font-size:9px;font-weight:600}
.pager .on{border-bottom:1px solid var(--white);padding-bottom:2px}
.pager .rail{width:72px;height:1px;background:rgba(255,255,255,.6)}

/* mission */
.mission-label{left:184px;top:656px;color:#444}
.mission-title{left:184px;top:680px;width:320px}
.mission-text{left:184px;top:744px;width:520px;color:var(--muted)}
.mission-more{left:905px;top:757px;color:var(--ink)}
.card{top:830px;width:266px;height:375px}
.card-1{left:184px;background:linear-gradient(180deg,#9a9a9c 0%,#5c5c60 55%,#1d1d1f 100%)}
.card-2{left:467px;background:linear-gradient(180deg,#f2f2f2 0%,#dcd8d2 45%,#8b6a4c 65%,#c9d2d6 100%)}
.card-3{left:750px;background:linear-gradient(180deg,#f4f4f4 0%,#d4d4d4 50%,#9a9a98 100%)}
.card-copy{left:184px;top:1030px;width:266px;text-align:center;color:var(--white)}
.card-copy h3{font-family:var(--serif);font-weight:700;font-size:16px}
.card-copy p{margin:12px auto 0;width:200px;font-size:10px;line-height:15px}
.card-copy .link-arrow{margin-top:22px}

/* about */
.about-dark{left:0;top:1300px;width:595px;height:347px;background:var(--black)}
.about-photo{left:595px;top:1300px;width:605px;height:347px;background:linear-gradient(120deg,#dcdcd8 0%,#b7b7b2 40%,#e8e2d6 70%,#c9c4ba 100%)}
.about-copy{left:181px;top:1385px;width:360px;color:var(--white)}
.about-copy .h2{margin-top:10px;color:var(--white)}
.about-copy .body{margin-top:10px}
.sign{text-align:right;margin-top:28px;font-size:10.5px}
.sign b{font-family:var(--serif);font-weight:700;display:block;margin-bottom:5px}

/* why */
.black-band{left:0;top:2144px;width:1200px;height:140px;background:var(--black)}
.why-panel{left:496px;top:1647px;width:704px;height:533px;background:var(--grey-panel)}
.why-photo{left:0;top:1743px;width:592px;height:345px;background:linear-gradient(180deg,#8e9ad0 0%,#c7b8d4 35%,#5f6778 60%,#7b7f86 80%,#4b5a44 100%)}
.count-box{left:446px;top:1852px;width:183px;height:132px;background:var(--white);text-align:center;padding-top:30px}
.count-box b{font-family:var(--serif);font-weight:400;font-size:50px;line-height:56px;display:block}
.count-box span{font-size:10px;color:var(--muted)}
.why-copy{left:645px;top:1809px;width:360px}
.why-copy .h2{margin-top:10px}
.why-copy .body{margin-top:14px;color:var(--muted)}
.stats{left:645px;top:2002px;width:360px;display:flex;justify-content:space-between;text-align:center;padding:0 0 0 8px}
.stats div{width:118px}
.stats b{font-family:var(--serif);font-weight:400;font-size:28px;display:block;line-height:34px}
.stats span{font-size:10px;color:var(--muted)}

/* enquiry */
.enquiry{left:295px;top:2246px;width:611px;height:322px;background:var(--white);box-shadow:0 6px 18px rgba(0,0,0,.18)}
.enquiry-photo{left:653px;top:2246px;width:253px;height:322px;background:linear-gradient(180deg,#b7d0ea 0%,#a8aeb4 40%,#8d5a48 60%,#e7e7e7 80%,#6f8a5a 100%)}
.enquiry-copy{left:330px;top:2300px}
.enquiry-copy .h2{margin-top:10px;font-size:19px}
.field{background:var(--field);font-size:10px;color:#8a8a8a;padding:7px 10px}
.f-name{left:328px;top:2367px;width:143px;height:27px}
.f-mail{left:476px;top:2367px;width:144px;height:27px}
.f-msg{left:328px;top:2405px;width:292px;height:79px}
.send{left:328px;top:2494px;width:292px;height:33px;background:var(--black);color:var(--white);font-size:9.5px;font-weight:600;letter-spacing:1px;display:flex;align-items:center;justify-content:center;gap:5px}

/* contact */
.contact-icon{left:191px;top:2637px;width:91px;height:88px;background:#ececec}
.contact-copy{left:302px;top:2630px;width:605px}
.contact-copy .h2{font-size:19px}
.contact-copy .body{margin-top:14px;color:var(--muted);font-size:10px;line-height:15px}

/* footer */
.footer{left:0;top:2784px;width:1200px;height:230px;background:var(--black);color:var(--white)}
.foot-h{font-family:var(--serif);font-weight:400;font-size:14px;letter-spacing:.5px;text-transform:uppercase}
.foot-nav{left:178px;top:2840px}
.foot-nav ul{list-style:none;margin-top:14px;font-size:10.5px;font-weight:600;line-height:21px}
.foot-contact{left:349px;top:2840px;width:270px}
.foot-contact p{margin-top:14px;font-size:10.5px;line-height:15px}
.foot-social{display:flex;gap:9px;margin-top:12px}
.foot-social i{width:16px;height:16px;border:1px solid var(--white);border-radius:50%;display:block}
.foot-logo{left:790px;top:2784px;width:228px;height:165px;background:var(--white);display:flex;align-items:center;justify-content:center;color:var(--ink)}
.foot-logo .brand{font-size:22px}
.foot-logo .brand i{width:14px;height:14px}
</style>
</head>
<body>

<!-- Hero -->
<div class="ph hero" role="img" aria-label="Two-storey grey weatherboard family home at sunset with lit windows and front garden"></div>
<div class="abs topbar">
  <div class="info">
    <span><svg width="10" height="10" viewBox="0 0 10 10"><path d="M2 1l2 2-1 1.3c.6 1.2 1.5 2.1 2.7 2.7L7 6l2 2-1.3 1.5C4.5 9 1 5.5.5 2.3z" fill="#fff"/></svg>(02) 5550 1834</span>
    <span><svg width="10" height="8" viewBox="0 0 10 8"><rect x=".5" y=".5" width="9" height="7" fill="none" stroke="#fff"/><path d="M.5.5L5 4.5 9.5.5" fill="none" stroke="#fff"/></svg>hello@varrow.example</span>
    <span><svg width="8" height="10" viewBox="0 0 8 10"><path d="M4 0a3.5 3.5 0 0 0-3.5 3.5C.5 6 4 10 4 10s3.5-4 3.5-6.5A3.5 3.5 0 0 0 4 0z" fill="#fff"/><circle cx="4" cy="3.5" r="1.2" fill="#8f93c6"/></svg>48 Tallow Lane, New South Wales</span>
  </div>
  <div class="social"><i></i><i></i><i></i></div>
</div>
<div class="abs nav">
  <div class="brand"><i></i>Varrow</div>
  <nav class="menu"><span>Home Designs</span><span>Display Homes</span><span>Custom Build</span><span>Knock Down Rebuild</span></nav>
</div>
<div class="abs hero-box">
  <h1>Exquisite Designs<br>at Prices You’ll Love</h1>
  <p>Experience the perfect blend of elegance and affordability with our carefully curated spaces designed to meet the highest standards of style and comfort. Whether you’re looking to enhance your home or business environment.</p>
  <div class="pager"><span>01</span><span class="on">02</span><span>03</span><span class="rail"></span>
    <svg width="30" height="10" viewBox="0 0 30 10"><path d="M5 1L1 5l4 4M25 1l4 4-4 4" fill="none" stroke="#fff" stroke-width="1.3"/></svg>
  </div>
</div>

<!-- Mission -->
<div class="abs label mission-label">Our Misssion.</div>
<h2 class="abs h2 mission-title">Discover the joy of your dream home with us...</h2>
<p class="abs body mission-text">Experience the perfect blend of elegance and affordability with our carefully curated spaces designed to meet the highest standards of style and comfort. Whether you’re looking to enhance your home or business environment.</p>
<div class="abs mission-more"><span class="link-arrow">More about us <svg width="12" height="6" viewBox="0 0 12 6"><path d="M0 3h11M8 .5L11 3 8 5.5" fill="none" stroke="#111"/></svg></span></div>

<div class="ph card card-1" role="img" aria-label="Modern grey kitchen interior, darkened behind project text"></div>
<div class="ph card card-2" role="img" aria-label="Bright kitchen with timber dining table and pendant lights"></div>
<div class="ph card card-3" role="img" aria-label="White open-plan kitchen with woven pendant lights"></div>
<div class="abs card-copy">
  <h3>Our houseing project 01</h3>
  <p>Nestled in the heart of Sydney, this exclusive housing project offers a perfect blend of luxury, comfort, and convenience.</p>
  <span class="link-arrow">Read more <svg width="12" height="6" viewBox="0 0 12 6"><path d="M0 3h11M8 .5L11 3 8 5.5" fill="none" stroke="#fff"/></svg></span>
</div>

<!-- About -->
<div class="abs about-dark"></div>
<div class="ph about-photo" role="img" aria-label="Smiling man working at a desk computer in a bright office"></div>
<div class="abs about-copy">
  <div class="label">About us.</div>
  <h2 class="h2">We believe we are enablers of people's dream homes.</h2>
  <p class="body">We pride ourselves on understanding the unique needs of our clients and delivering homes that exceed expectations. Our team of experienced professionals works closely with you at every stage, ensuring that your home is not just built but crafted with care, precision, and passion.</p>
  <div class="sign"><b>Marten Hale</b>Chairman, Varrow Constructions</div>
</div>

<!-- Why -->
<div class="abs black-band"></div>
<div class="abs why-panel"></div>
<div class="ph why-photo" role="img" aria-label="Grey two-storey home with three-car garage at dusk"></div>
<div class="abs count-box"><b>65</b><span>Complete projects</span></div>
<div class="abs why-copy">
  <div class="label" style="color:#555">Why us.</div>
  <h2 class="h2">Why Choose Us</h2>
  <p class="body">Choosing the right builder is crucial to your home-building journey. At Varrow, we stand out with our unwavering dedication to excellence, transparency, and customer satisfaction. With years of experience and a reputation for delivering on our promises, we ensure that your experience with us is as smooth and rewarding as possible. Discover why so many trust us to build their dream homes.</p>
</div>
<div class="abs stats">
  <div><b>10</b><span>Team members</span></div>
  <div><b>80</b><span>Happy clients</span></div>
  <div><b>15</b><span>Projects underway</span></div>
</div>

<!-- Enquiry -->
<div class="abs enquiry"></div>
<div class="ph enquiry-photo" role="img" aria-label="Brick and weatherboard townhouse with double white garage doors"></div>
<div class="abs enquiry-copy">
  <div class="label" style="color:#555">Quick enquiry.</div>
  <h2 class="h2">Want more information?</h2>
</div>
<div class="abs field f-name">Your name</div>
<div class="abs field f-mail">Your email</div>
<div class="abs field f-msg">Message</div>
<div class="abs send">SEND MESSAGE <svg width="10" height="6" viewBox="0 0 10 6"><path d="M0 3h9M6.5.5L9 3 6.5 5.5" fill="none" stroke="#fff"/></svg></div>

<!-- Contact -->
<div class="ph contact-icon" role="img" aria-label="Line drawing of a small house"></div>
<div class="abs contact-copy">
  <h2 class="h2">Contact us</h2>
  <p class="body">Ready to start your journey with Varrow? Whether you have questions, need more information, or are ready to take the first step in building your dream home, we’re here to help. Reach out to us today, and let’s begin the process of turning your vision into reality. We’re just a phone call or email away!</p>
</div>

<!-- Footer -->
<footer class="abs footer"></footer>
<div class="abs foot-nav" style="color:#fff">
  <div class="foot-h">Navigation</div>
  <ul><li>Home Designs</li><li>Display Homes</li><li>Custom Build</li><li>Knock Down Rebuild</li></ul>
</div>
<div class="abs foot-contact" style="color:#fff">
  <div class="foot-h">Contact us</div>
  <p>Our team is dedicated to making your home-building journey as smooth and enjoyable as possible.</p>
  <div class="foot-social"><i></i><i></i><i></i></div>
</div>
<div class="abs foot-logo"><div class="brand"><i></i>Varrow</div></div>

</body>
</html>
```